Agency Website & Personal brand

My name is Petros Valtinos & I've been a digital marketer & an e-commerce expert since 2010.

- I've spoken to 20 different events around the world up to 3,000 people in size.
- I've sold over 1500 training courses around e-commerce growth.
- I have over 100 testimonials (video & photo) from successful students who bought my training
- I have dozens of video testimonials from respected entrepreneurs that vouch for me and my work
- I have photos with marketing legends with that I shared the stage like Owen Farrow, Thomas Brennigan, Colin Marsh & more
- I am the host of the Aegean Roundtable since 2017 - a high-level networking event for 7 & 8 figure entrepreneurs - 100 people have come to Greece since 2017
- I have tons of videos created where I showcase my expertise on growth
- I have worked with dozens of e-commerce stores on their growth & helped them scale to multiple 6, 7 & 8 figures either on consulting

I need a website design that showcases my authority & be a lead generating machine.

The goal is to bring people on a call with me but also grab their email and start building the relationship with them and free valuable content

We have 3 offers :

1. Paid ads (Done for You)
2. Consulting/Mastermind (Done with You)
3. Training (Do it Yourself)

```html
<!DOCTYPE html>
<html lang="en">
<head>
<meta charset="utf-8">
<title>Petros Valtinos — Digital Marketer &amp; E-commerce Expert</title>
<link rel="stylesheet" href="https://fonts.googleapis.com/css2?family=Cinzel:wght@400;500&family=Montserrat:ital,wght@0,400;0,500;0,600;0,700;1,400&display=swap">
<style>
:root{
  --blue:#3b6fdc;
  --ink:#1c1c1c;
  --text:#444;
  --white:#fff;
  --black:#050505;
}
*{box-sizing:border-box;margin:0;padding:0}
html,body{width:1200px;height:3670px;overflow:hidden}
body{font-family:"Montserrat",Arial,sans-serif;color:var(--text);background:var(--white);position:relative}
section,header,footer{position:absolute;left:0;width:1200px}

/* header */
.site-header{top:0;height:74px;background:var(--white);border-top:3px solid var(--blue)}
.brand{position:absolute;font-family:"Cinzel",Georgia,serif;color:var(--blue);font-weight:500;letter-spacing:1px;line-height:1;display:flex;align-items:center;gap:8px;white-space:nowrap}
.brand-mark{width:12px;height:12px;background:var(--blue)}
.site-header .brand{left:164px;top:26px;font-size:19px}
.nav a{position:absolute;top:34px;font-size:11px;font-weight:600;color:var(--ink);text-decoration:none;letter-spacing:.3px;white-space:nowrap}
.call{position:absolute;left:889px;top:21px;display:flex;align-items:center;gap:10px}
.call-icon{width:34px;height:34px;border-radius:50%;background:var(--blue);display:flex;align-items:center;justify-content:center}
.call small{display:block;font-size:8.5px;font-weight:600;color:var(--ink)}
.call strong{display:block;font-size:15px;color:var(--blue);font-weight:700;margin-top:2px}

/* hero */
.hero{top:74px;height:500px;background:linear-gradient(120deg,#3468d6 0%,#2c5fcf 45%,#3d72de 100%);overflow:hidden}
.hero h1{position:absolute;left:162px;top:110px;font-family:"Cinzel",Georgia,serif;font-weight:400;font-size:40px;line-height:49px;color:var(--white);letter-spacing:.5px}
.hero .rule{position:absolute;left:162px;top:271px;width:228px;height:2px;background:var(--white)}
.hero p{position:absolute;left:162px;top:290px;width:400px;font-size:11.5px;line-height:22px;color:var(--white)}
.btn{display:flex;align-items:center;justify-content:center;font-family:"Cinzel",Georgia,serif;font-size:13px;letter-spacing:1px;text-decoration:none}
.hero .btn{position:absolute;left:162px;top:346px;width:136px;height:33px;background:var(--white);color:var(--blue)}
.hero-photo{position:absolute;left:563px;top:68px;width:637px;height:432px;background:radial-gradient(ellipse at 50% 60%,#5a5f6e 0%,#3d4e80 40%,rgba(44,95,207,0) 72%)}

/* about */
.about{top:574px;height:691px;background:var(--white)}
.about-band{position:absolute;left:0;top:0;width:462px;height:691px;background:var(--blue)}
.about-photo{position:absolute;left:161px;top:74px;width:460px;height:546px;background:linear-gradient(160deg,#d9d4cc 0%,#a89c8c 45%,#4a4038 100%)}
.eyebrow{font-size:16px;font-weight:700;color:var(--blue);letter-spacing:.3px}
.about-copy{position:absolute;left:705px;top:146px;width:320px;display:flex;flex-direction:column;align-items:flex-start}
.about-copy h2{font-family:"Cinzel",Georgia,serif;font-weight:500;font-size:26px;color:var(--ink);margin-top:2px;white-space:nowrap}
.about-copy .rule{width:230px;height:2px;background:var(--blue);margin-top:8px}
.about-copy p{margin-top:12px;width:318px;font-size:10.5px;line-height:21.8px;text-align:justify;color:var(--text)}
.about-copy .btn{margin-top:12px;width:136px;height:32px;background:var(--blue);color:var(--white)}

/* section heads */
.head{position:absolute;left:0;width:1200px;text-align:center}
.head .eyebrow{display:block}
.head h2{font-family:"Cinzel",Georgia,serif;font-weight:400;font-size:28px;color:var(--ink);margin-top:4px;letter-spacing:.5px}
.head .rule{width:230px;height:2px;background:var(--blue);margin:10px auto 0}

/* works */
.works{top:1265px;height:663px;background:linear-gradient(180deg,#e6eaf2 0%,#dfe4ee 50%,#e9ecf3 100%)}
.works .head{top:82px}
.work-card{position:absolute;width:208px;height:184px;background:var(--white);text-align:center;color:var(--ink);box-shadow:0 2px 8px rgba(0,0,0,.05)}
.work-card svg{margin-top:22px}
.work-card p{font-size:12.5px;font-weight:600;line-height:22px;margin:8px 14px 0}
.work-card.is-active{background:var(--blue);color:var(--white)}

/* services */
.services{top:1928px;height:570px;background:var(--white)}
.services .head{top:66px}
.service-card{position:absolute;top:163px;width:272px;height:322px;border-radius:30px;background:var(--white);box-shadow:0 3px 14px rgba(40,60,120,.16);text-align:center}
.service-card .icon{width:90px;height:90px;border-radius:50%;background:var(--blue);margin:20px auto 0;display:flex;align-items:center;justify-content:center}
.service-card h3{font-weight:400;font-size:17px;line-height:22px;color:var(--blue);margin-top:24px}
.service-card p{font-size:10.5px;line-height:22px;margin:10px 12px 0;color:var(--text)}
.service-card.is-active{background:var(--blue)}
.service-card.is-active .icon{background:var(--white)}
.service-card.is-active h3,.service-card.is-active p{color:var(--white)}

/* testimonials */
.testimonials{top:2498px;height:469px;background:var(--white)}
.testimonials .head{top:60px}
.video-main{position:absolute;left:162px;top:165px;width:415px;height:244px;background:linear-gradient(180deg,#c9c6c0 0%,#8f8e8c 50%,#3d3f45 100%)}
.play{position:absolute;border-radius:50%;border:2px solid var(--white);display:flex;align-items:center;justify-content:center}
.quote-block{position:absolute;left:612px;top:180px;width:380px;text-align:center}
.quote{font-style:italic;font-size:10px;line-height:19.5px;color:#555}
.quote-author{margin-top:6px;font-family:"Cinzel",Georgia,serif;font-size:19px;line-height:22px;color:var(--blue)}
.thumb{position:absolute;top:325px;width:138px;height:84px}

/* contact */
.contact{top:2967px;height:400px;background:linear-gradient(120deg,#3a6dda,#3267d6);overflow:hidden}
.contact .head{top:52px}
.contact .head .eyebrow,.contact .head h2{color:var(--white)}
.contact .head .rule{background:var(--white)}
.contact-item{position:absolute;left:245px;display:flex;align-items:flex-start;gap:14px;color:var(--white);font-size:11px;line-height:22px}
.contact-item svg{flex:none;margin-top:2px}
.field{position:absolute;background:var(--white);font-size:10px;color:#777;padding:10px 9px}
.contact .btn{position:absolute;left:557px;top:315px;width:136px;height:34px;border:1.5px solid var(--white);color:var(--white)}

/* footer */
.site-footer{top:3367px;height:303px;background:var(--black);text-align:center}
.site-footer .brand{left:0;width:1200px;justify-content:center;top:68px;font-size:34px}
.footer-nav{position:absolute;top:169px;left:0;width:1200px;display:flex;justify-content:center;gap:32px}
.footer-nav a{font-size:10.5px;font-weight:700;color:var(--white);text-decoration:none}
.copyright{position:absolute;top:200px;left:0;width:1200px;font-size:10px;font-weight:600;color:var(--white)}
.social{position:absolute;top:235px;left:0;width:1200px;display:flex;justify-content:center;gap:8px}
.social span{width:27px;height:27px;border-radius:50%;background:var(--blue);border:2px solid var(--white)}
</style>
</head>
<body>

<header class="site-header">
  <div class="brand"><span>PETROS VALTINOS</span><span class="brand-mark"></span></div>
  <nav class="nav">
    <a href="#" style="left:422px">HOME</a>
    <a href="#" style="left:487px">ABOUT US</a>
    <a href="#" style="left:574px">OUR SERVICES</a>
    <a href="#" style="left:685px">TESTIMONIALS</a>
    <a href="#" style="left:797px">CONTACT US</a>
  </nav>
  <div class="call">
    <span class="call-icon"><svg width="16" height="16" viewBox="0 0 24 24"><path fill="#fff" d="M6.6 10.8a15.1 15.1 0 0 0 6.6 6.6l2.2-2.2c.3-.3.7-.4 1-.2 1.1.4 2.3.6 3.6.6.6 0 1 .4 1 1V20c0 .6-.4 1-1 1A17 17 0 0 1 3 4c0-.6.4-1 1-1h3.5c.6 0 1 .4 1 1 0 1.3.2 2.5.6 3.6.1.3 0 .7-.2 1z"/></svg></span>
    <div><small>CALL US TODAY</small><strong>(123) 456 7890</strong></div>
  </div>
</header>

<section class="hero">
  <h1>DIGITAL MARKETER<br>&amp; AN E-COMMERCE<br>EXPERT SINCE 2010</h1>
  <div class="rule"></div>
  <p>Lorem ipsum dolor sit amet, consectetur adipiscing elit, sed do eius mod tempor incididunt ut labore et dolore magna aliqua.</p>
  <a class="btn" href="#">GET STARTED</a>
  <div class="hero-photo" role="img" aria-label="Photo of Petros Valtinos on stage with arms outstretched, wearing a headset microphone"></div>
</section>

<section class="about">
  <div class="about-band"></div>
  <div class="about-photo" role="img" aria-label="Photo of Petros Valtinos speaking with a microphone in a bright room"></div>
  <div class="about-copy">
    <span class="eyebrow">ABOUT ME</span>
    <h2>HI I'M PETROS VALTINOS</h2>
    <div class="rule"></div>
    <p>Lorem ipsum dolor sit amet, consectetur adipiscing elit, sed do eiusmod tempor incididunt ut labore et dolore magna aliqua.perspiciatis unde omnis iste natus error sit voluptatem accusantium doloremque laudantium, totam rem aperiam, eaque ipsa quae ab illo inventore veritatis et quasi architecto beatae vitae dicta sunt explicabo. Nemo enim ipsam voluptatem quia voluptas sit aspernatur aut odit aut fugit, sed quia consequuntur magni dolores eos qui ratione voluptatem sequi nesciunt. Neque porro quisquam est, qui dolorem ipsum quia dolor sit amet, consectetur, adipisci velit, sed quia non numquam eius modi tempora incidunt ut labore et dolore magnam aliquam quaerat voluptatem.</p>
    <a class="btn" href="#">GET STARTED</a>
  </div>
</section>

<section class="works">
  <div class="head"><span class="eyebrow">MY WORKS</span><h2>LOREM IPSUM DOLOR SIT AMET CONSECTETUR ADIPIS</h2><div class="rule"></div></div>

  <div class="work-card" style="left:162px;top:187px">
    <svg width="68" height="64" viewBox="0 0 68 64" fill="none" stroke="#3b6fdc" stroke-width="2.5"><rect x="3" y="8" width="56" height="48" rx="4"/><line x1="3" y1="20" x2="59" y2="20"/><line x1="16" y1="3" x2="16" y2="13"/><line x1="31" y1="3" x2="31" y2="13"/><line x1="46" y1="3" x2="46" y2="13"/><rect x="11" y="27" width="7" height="6"/><rect x="24" y="27" width="7" height="6"/><rect x="37" y="27" width="7" height="6"/><rect x="11" y="39" width="7" height="6"/><rect x="24" y="39" width="7" height="6"/><circle cx="53" cy="51" r="11" fill="#fff"/><path d="M48 51l4 4 7-8"/></svg>
    <p>20 different events around the world up to 3,000 people in size.</p>
  </div>
  <div class="work-card is-active" style="left:385px;top:187px">
    <svg width="68" height="64" viewBox="0 0 68 64" fill="none" stroke="#fff" stroke-width="2.5"><rect x="10" y="8" width="48" height="38" rx="3"/><path d="M4 52h60l-4 6H8z"/><path d="M20 24l14-7 14 7-14 7z"/><path d="M25 27v7c5 4 13 4 18 0v-7"/></svg>
    <p>1500 training courses around e-commerce growth.</p>
  </div>
  <div class="work-card" style="left:607px;top:187px">
    <svg width="68" height="64" viewBox="0 0 68 64" fill="none" stroke="#3b6fdc" stroke-width="2.5"><path d="M14 14h42a8 8 0 0 1 8 8v20a8 8 0 0 1-8 8H30l-12 10v-10h-4a8 8 0 0 1-8-8V22"/><line x1="24" y1="28" x2="54" y2="28"/><line x1="24" y1="35" x2="54" y2="35"/><line x1="24" y1="42" x2="46" y2="42"/><path d="M4 4h7v7H7v4M14 4h7v7h-4v4"/></svg>
    <p>100 testimonials from successful students who bought my training</p>
  </div>
  <div class="work-card" style="left:829px;top:187px">
    <svg width="68" height="64" viewBox="0 0 68 64" fill="none" stroke="#3b6fdc" stroke-width="2.5"><circle cx="34" cy="16" r="11"/><path d="M14 62V46c0-8 8-14 20-14s20 6 20 14v16"/><path d="M30 34l4 12 4-12"/><rect x="22" y="48" width="24" height="14"/></svg>
    <p>Host of the Aegean Roundtable since 2017 - a high-level networking.</p>
  </div>
  <div class="work-card" style="left:385px;top:391px">
    <svg width="76" height="64" viewBox="0 0 76 64" fill="none" stroke="#3b6fdc" stroke-width="2.5"><rect x="3" y="3" width="70" height="58" rx="4"/><line x1="3" y1="46" x2="73" y2="46"/><path d="M32 16l14 9-14 9z"/><line x1="10" y1="54" x2="66" y2="54"/><circle cx="26" cy="54" r="3" fill="#fff"/></svg>
    <p>Tons of videos created where I showcase my expertise on growth.</p>
  </div>
  <div class="work-card" style="left:607px;top:391px">
    <svg width="68" height="64" viewBox="0 0 68 64" fill="none" stroke="#3b6fdc" stroke-width="2.5"><path d="M18 24a16 16 0 0 1 32 0"/><rect x="13" y="22" width="7" height="13" rx="3"/><rect x="48" y="22" width="7" height="13" rx="3"/><path d="M51 35c0 6-5 9-12 9"/><path d="M10 62V54c0-6 10-10 24-10s24 4 24 10v8"/></svg>
    <p>e-commerce stores on their growth &amp; helped them scale to multiple.</p>
  </div>
</section>

<section class="services">
  <div class="head"><span class="eyebrow">WHAT WE DO</span><h2>LOREM IPSUM DOLOR SIT AMET CONSECTETUR ADIPIS</h2><div class="rule"></div></div>

  <div class="service-card" style="left:162px">
    <div class="icon"><svg width="48" height="44" viewBox="0 0 48 44" fill="none" stroke="#fff" stroke-width="2"><rect x="3" y="6" width="38" height="34" rx="3"/><line x1="3" y1="13" x2="41" y2="13"/><rect x="11" y="20" width="22" height="12"/><text x="22" y="29.5" fill="#fff" stroke="none" font-family="Montserrat,sans-serif" font-size="8" font-weight="600" text-anchor="middle">Ads</text><circle cx="40" cy="8" r="6" fill="#3b6fdc"/><text x="40" y="11" fill="#fff" stroke="none" font-family="Montserrat,sans-serif" font-size="8" text-anchor="middle">$</text></svg></div>
    <h3>Paid ads<br>(Done for You)</h3>
    <p>Lorem ipsum dolor sit amet, consectetur adipiscing elit, sed do eiusmod tempor incididunt ut labore et dolore magna aliqua. Ut enim ad minim veniam, quis nostrud exercitation ullamco laboris nisi ut aliqui.</p>
  </div>
  <div class="service-card is-active" style="left:465px">
    <div class="icon"><svg width="48" height="44" viewBox="0 0 48 44" fill="none" stroke="#3b6fdc" stroke-width="2"><rect x="20" y="2" width="20" height="12" rx="2"/><circle cx="16" cy="14" r="4"/><path d="M8 30v-6c0-3 4-5 8-5s8 2 8 5v6"/><line x1="4" y1="30" x2="44" y2="30"/><line x1="10" y1="30" x2="10" y2="42"/><line x1="38" y1="30" x2="38" y2="42"/><rect x="28" y="20" width="12" height="10"/></svg></div>
    <h3>Consulting/Mastermind<br>(Done with You)</h3>
    <p>Lorem ipsum dolor sit amet, consectetur adipiscing elit, sed do eiusmod tempor incididunt ut labore et dolore magna aliqua. Ut enim ad minim veniam, quis nostrud exercitation ullamco laboris nisi ut aliqui.</p>
  </div>
  <div class="service-card" style="left:765px">
    <div class="icon"><svg width="48" height="44" viewBox="0 0 48 44" fill="none" stroke="#fff" stroke-width="2"><rect x="12" y="2" width="32" height="20"/><line x1="18" y1="9" x2="38" y2="9"/><line x1="18" y1="15" x2="32" y2="15"/><circle cx="6" cy="10" r="3"/><path d="M3 22v-6h6l5-3"/><circle cx="8" cy="30" r="3"/><circle cx="19" cy="30" r="3"/><circle cx="30" cy="30" r="3"/><circle cx="41" cy="30" r="3"/><path d="M4 42v-5h8v5M15 42v-5h8v5M26 42v-5h8v5M37 42v-5h8v5"/></svg></div>
    <h3>Training<br>(Do it Yourself)</h3>
    <p>Lorem ipsum dolor sit amet, consectetur adipiscing elit, sed do eiusmod tempor incididunt ut labore et dolore magna aliqua. Ut enim ad minim veniam, quis nostrud exercitation ullamco laboris nisi ut aliqui.</p>
  </div>
</section>

<section class="testimonials">
  <div class="head"><span class="eyebrow">TESTIMONIALS</span><h2>OUR CLIENT TESTIMONIALS</h2><div class="rule"></div></div>
  <div class="video-main" role="img" aria-label="Video still of two men in conversation seated in a studio with a camera">
    <div class="play" style="left:183px;top:98px;width:50px;height:50px;background:rgba(59,111,220,.55)"><svg width="18" height="18" viewBox="0 0 18 18"><path d="M5 3l10 6-10 6z" fill="none" stroke="#fff" stroke-width="2"/></svg></div>
  </div>
  <div class="quote-block">
    <p class="quote">Lorem ipsum dolor sit amet, consectetur adipiscing elit, sed do eiusmod tempor incididunt ut labore et dolore magna aliqua. Ut enim ad minim veniam, quis nostrud exercitation ullamco laboris nisi ut aliquip ex ea commodo consequat. Duis aute irure dolor in reprehenderit in voluptate velit esse cillum dolore eu fugiat nulla pariatur.</p>
    <div class="quote-author">- John Deo</div>
  </div>
  <div class="thumb" style="left:600px;background:#4f7ee0" role="img" aria-label="Video thumbnail of a testimonial">
    <div class="play" style="left:57px;top:30px;width:24px;height:24px"><svg width="10" height="10" viewBox="0 0 10 10"><path d="M2 1l7 4-7 4z" fill="#fff"/></svg></div>
  </div>
  <div class="thumb" style="left:745px;background:linear-gradient(180deg,#1a1a1a,#3a3526 70%,#c9a23a)" role="img" aria-label="Photo of a Q&amp;A session on stage"></div>
  <div class="thumb" style="left:892px;background:linear-gradient(160deg,#6b4a32,#2c1d14 70%,#1a1410)" role="img" aria-label="Photo of a speaker presenting on stage"></div>
</section>

<section class="contact">
  <div class="head"><span class="eyebrow">CONTACT US</span><h2>LOREM IPSUM DOLOR SIT AMET CONSECTETUR ADIPIS</h2><div class="rule"></div></div>

  <div class="contact-item" style="top:166px"><svg width="20" height="24" viewBox="0 0 20 24"><path fill="#fff" d="M10 0a9 9 0 0 0-9 9c0 7 9 15 9 15s9-8 9-15a9 9 0 0 0-9-9zm0 13a4 4 0 1 1 0-8 4 4 0 0 1 0 8z"/></svg><span>123 Lorem ipsum dolor sit amet, con-<br>sectetur adipiscing.</span></div>
  <div class="contact-item" style="top:220px"><svg width="20" height="20" viewBox="0 0 24 24"><path fill="#fff" d="M6.6 10.8a15.1 15.1 0 0 0 6.6 6.6l2.2-2.2c.3-.3.7-.4 1-.2 1.1.4 2.3.6 3.6.6.6 0 1 .4 1 1V20c0 .6-.4 1-1 1A17 17 0 0 1 3 4c0-.6.4-1 1-1h3.5c.6 0 1 .4 1 1 0 1.3.2 2.5.6 3.6.1.3 0 .7-.2 1z"/></svg><span>+1 888 888 8888</span></div>
  <div class="contact-item" style="top:266px"><svg width="20" height="16" viewBox="0 0 20 16"><rect x="0" y="0" width="20" height="16" rx="1" fill="#fff"/><path d="M1 2l9 7 9-7" fill="none" stroke="#3b6fdc" stroke-width="1.6"/></svg><span>info@petrosvaltinos.com</span></div>
  <div class="contact-item" style="top:311px"><svg width="20" height="20" viewBox="0 0 20 20" fill="none" stroke="#fff" stroke-width="1.6"><circle cx="10" cy="10" r="9"/><ellipse cx="10" cy="10" rx="4" ry="9"/><line x1="1" y1="10" x2="19" y2="10"/><line x1="2.5" y1="5.5" x2="17.5" y2="5.5"/><line x1="2.5" y1="14.5" x2="17.5" y2="14.5"/></svg><span>www.petrosvaltinos.com</span></div>

  <div class="field" style="left:557px;top:146px;width:197px;height:32px">First Name</div>
  <div class="field" style="left:762px;top:146px;width:194px;height:32px">Last Name</div>
  <div class="field" style="left:557px;top:187px;width:197px;height:32px">Email:</div>
  <div class="field" style="left:762px;top:187px;width:194px;height:32px">Phone:</div>
  <div class="field" style="left:557px;top:226px;width:399px;height:69px">Message:</div>
  <a class="btn" href="#">SUBMIT NOW</a>
</section>

<footer class="site-footer">
  <div class="brand"><span>PETROS VALTINOS</span><span class="brand-mark"></span></div>
  <nav class="footer-nav">
    <a href="#">HOME</a><a href="#">ABOUT US</a><a href="#">OUR SERVICES</a><a href="#">TESTIMONIALS</a><a href="#">CONTACT US</a>
  </nav>
  <p class="copyright">© 2023 PETROS VALTINOS &nbsp;|&nbsp; ALL RIGHTS RESERVED.</p>
  <div class="social" aria-label="Social profiles"><span></span><span></span><span></span><span></span></div>
</footer>

</body>
</html>
```